Fun Social App Need Simple, Logo, Clean App Design, and Icon

We need a app design for a new social meet up, planning app called Brindle. The look and feel should be fun, yet clean and simple. This is an app for setting up meetings with friends and family. Our motto is Meet Up On A Whim. What we need:

-Logo

-App Icon

-Layout App pages as shown in attached. (Most will use the same header you come up with, with perhaps a few extras as you wish to add on each page)

-A button design that can be used throughout the app that conveys "push me" We will use this button in several places and simply change the text on it.
Updates

https://pelwarkdigest.com/blog/58213-20-striking-samples-of-sparse-phone-screen-layouts#k.7x2mqvtrelaguz We like the minimalist look.

Target Market(s)

Ages 10-39 Primarily

Industry/Entity Type

Social

Font styles to use
Sans Serif

Colors

Designer to choose colors to be used in the design.

Requirements
Must have
• Would like to focus on the S in the logo/icon. A S with arrows at both tips would be good.

```html
<!DOCTYPE html>
<html lang="en">
<head>
<meta charset="utf-8">
<title>Brindle – Welcome</title>
<link rel="stylesheet" href="https://fonts.googleapis.com/css2?family=Roboto+Condensed:wght@300;400;700&display=swap">
<style>
  :root {
    --brand-red: #e42f18;
    --white: #ffffff;
    --soft-peach: #f7a48c;
    --status-dim: #f4a08a;
    --type: "Roboto Condensed", "Helvetica Neue", Arial, sans-serif;
  }
  * { box-sizing: border-box; margin: 0; padding: 0; }
  html, body {
    width: 676px; height: 1200px; overflow: hidden;
    background: var(--brand-red);
  }
  .screen {
    position: absolute; left: 0; top: 0;
    width: 640px; height: 1136px;
    transform: scale(1.05625); transform-origin: 0 0;
    background: var(--brand-red);
    font-family: var(--type);
    color: var(--white);
  }
  .status-bar {
    position: absolute; left: 0; top: 0; width: 640px; height: 40px;
    font-size: 22px; font-weight: 400; letter-spacing: 0.5px;
  }
  .status-bar .signal { position: absolute; left: 10px; top: 13px; }
  .status-bar .carrier { position: absolute; left: 87px; top: 7px; }
  .status-bar .wifi { position: absolute; left: 153px; top: 9px; }
  .status-bar .clock { position: absolute; left: 0; width: 640px; top: 7px; text-align: center; font-size: 23px; }
  .status-bar .bluetooth { position: absolute; left: 481px; top: 7px; }
  .status-bar .charge { position: absolute; left: 513px; top: 7px; }
  .status-bar .battery { position: absolute; left: 579px; top: 10px; }

  .brand-lockup {
    position: absolute; left: 116px; top: 208px; width: 400px; height: 246px;
    background: var(--white); padding: 5px 5px 0 5px;
  }
  .brand-lockup .panel {
    width: 390px; height: 200px; background: var(--brand-red);
    display: flex; flex-direction: column; align-items: center;
    padding-top: 88px;
  }
  .brand-name {
    font-size: 62px; font-weight: 400; line-height: 1;
    color: var(--white);
  }
  .brand-tagline {
    margin-top: 10px; font-size: 22px; font-weight: 400; line-height: 1;
    letter-spacing: 1px; color: var(--soft-peach);
  }

  .btn {
    position: absolute; display: flex; align-items: center; justify-content: center;
    font-family: var(--type); font-size: 34px; font-weight: 700;
    text-decoration: none;
  }
  .btn-primary {
    left: 100px; top: 621px; width: 440px; height: 80px;
    background: var(--white); color: var(--brand-red);
  }
  .account-prompt {
    position: absolute; left: 0; top: 742px; width: 640px; text-align: center;
    font-size: 26px; font-weight: 300; color: var(--soft-peach);
  }
  .btn-secondary {
    left: 99px; top: 788px; width: 442px; height: 82px;
    border: 1px solid var(--soft-peach); color: var(--soft-peach);
  }
  .legal {
    position: absolute; left: 0; top: 1044px; width: 640px; text-align: center;
    font-size: 22px; font-weight: 400; line-height: 29px; color: var(--soft-peach);
  }
  .legal a { color: var(--white); text-decoration: underline; text-underline-offset: 3px; }
</style>
</head>
<body>
<main class="screen">
  <header class="status-bar">
    <svg class="signal" width="42" height="12" viewBox="0 0 42 12" aria-hidden="true">
      <circle cx="6" cy="6" r="5.5" fill="#fff"/><circle cx="20" cy="6" r="5.5" fill="#fff"/><circle cx="34" cy="6" r="5.5" fill="#fff"/>
    </svg>
    <span class="carrier">VALE</span>
    <svg class="wifi" width="24" height="20" viewBox="0 0 24 20" aria-hidden="true">
      <path d="M12 19 L2 7 A14 14 0 0 1 22 7 Z" fill="#fff"/>
    </svg>
    <span class="clock">4:21 PM</span>
    <svg class="bluetooth" width="16" height="26" viewBox="0 0 16 26" aria-hidden="true">
      <path d="M2 7 L13 18 L8 23 L8 3 L13 8 L2 19" fill="none" stroke="var(--status-dim)" stroke-width="2"/>
    </svg>
    <span class="charge">100%</span>
    <svg class="battery" width="50" height="20" viewBox="0 0 50 20" aria-hidden="true">
      <rect x="1" y="1" width="43" height="18" rx="2" fill="none" stroke="#fff" stroke-width="2"/>
      <rect x="3" y="3" width="39" height="14" fill="#fff"/>
      <rect x="45" y="6" width="3" height="8" fill="#fff"/>
    </svg>
  </header>

  <section class="brand-lockup">
    <div class="panel">
      <h1 class="brand-name">Brindle</h1>
      <p class="brand-tagline">Meet up on a whim</p>
    </div>
  </section>

  <a class="btn btn-primary" href="#">Sign Up</a>
  <p class="account-prompt">Already have an account?</p>
  <a class="btn btn-secondary" href="#">Login</a>

  <footer class="legal">
    By using brindle, you agree to the<br>
    <a href="#">Terms of Use</a> and <a href="#">Privacy Policy.</a>
  </footer>
</main>
</body>
</html>
```